Advertisement Design

I'm looking for a post card sized advertisement piece that I will be dropping off to commercial and residential customers.
On one side I want it promoting carpet cleaning services and on the other side dryer vent cleaning services.
I've uploaded two different layouts of my company logo for you to choice from.
One batch will be printed with my Michigan Number
One batch will be printed with my Tennessee number
Will share contact numbers with the winner so just use a make up number
555-319-4826

Slow in providing feedback

```html
<!DOCTYPE html>
<html lang="en">
<head>
<meta charset="UTF-8">
<title>Carpet Cleaning Postcard</title>
<link rel="stylesheet" href="https://fonts.googleapis.com/css2?family=Montserrat:wght@400;500;700;800&family=Oswald:wght@600&display=swap">
<style>
  :root {
    --bg: #e4e4e4;
    --white: #ffffff;
    --blue-light: #1a7bc0;
    --blue-mid: #1667ad;
    --blue-deep: #0d4a8f;
    --blue-navy: #0a3a80;
    --ink: #2b2b2b;
  }
  * { margin: 0; padding: 0; box-sizing: border-box; }
  html, body { width: 1200px; height: 1200px; overflow: hidden; background: var(--bg); }
  .postcard {
    position: absolute; left: 40px; top: 193px;
    width: 1120px; height: 814px;
    background: var(--white); overflow: hidden;
    font-family: "Montserrat", sans-serif;
    box-shadow: 0 6px 18px rgba(0,0,0,.18);
  }
  .hero-photo {
    position: absolute; left: 566px; top: 0; width: 554px; height: 571px;
    background: linear-gradient(172deg,
      #c9ced2 0%, #e3e5e6 18%, #a9afb5 38%, #4e5560 52%,
      #7c838b 62%, #cfd1d0 76%, #ecebe8 90%, #dcdcd9 100%);
  }
  .gallery-band {
    position: absolute; left: 566px; top: 571px; width: 554px; height: 123px;
    background: var(--blue-mid);
  }
  .accent-strip {
    position: absolute; left: 0; top: 671px; width: 1120px; height: 23px;
    background: var(--blue-navy);
  }
  .headline {
    position: absolute; left: 67px; top: 80px;
    font-size: 54px; line-height: 56px; letter-spacing: .3px;
  }
  .headline .light { display: block; font-weight: 500; color: var(--blue-light); }
  .headline .bold { display: block; font-weight: 800; color: var(--blue-deep); }
  .intro {
    position: absolute; left: 67px; top: 326px; width: 360px;
    font-size: 19.5px; line-height: 27.5px; color: var(--ink); font-weight: 500;
  }
  .service-list {
    position: absolute; left: 67px; top: 445px; list-style: none;
    font-size: 26.5px; line-height: 33px; color: var(--blue-mid); font-weight: 500;
  }
  .service-list li::before { content: "\00B7"; margin-right: 2px; }
  .call-rule {
    position: absolute; left: 69px; top: 599px; width: 440px; height: 4px;
    background: var(--blue-light);
  }
  .call-label {
    position: absolute; left: 74px; top: 620px;
    font-size: 35px; font-weight: 800; color: var(--blue-deep); letter-spacing: .5px;
  }
  .phone-bar { position: absolute; left: 0; top: 694px; width: 1120px; height: 120px; }
  .phone-number {
    position: absolute; left: 73px; top: 696px;
    font-family: "Oswald", sans-serif; font-weight: 600;
    font-size: 78px; line-height: 110px; color: var(--white); letter-spacing: -.5px;
  }
  .phone-icon { position: absolute; left: 27px; top: 738px; }
  .gallery { position: absolute; left: 0; top: 0; }
  .brand {
    position: absolute; left: 735px; top: 722px; height: 72px;
    display: flex; align-items: center; gap: 18px;
  }
  .brand-mark { width: 64px; height: 64px; background: var(--blue-light); }
  .brand-divider { width: 3px; height: 72px; background: #555; }
  .brand-name {
    font-size: 21px; line-height: 25px; font-weight: 700; color: var(--blue-deep);
    text-transform: uppercase; letter-spacing: .5px;
  }
</style>
</head>
<body>
  <div class="postcard">
    <div class="hero-photo" role="img" aria-label="Technician vacuuming a light carpet with a canister cleaner in a bright living room"></div>
    <div class="gallery-band"></div>
    <div class="accent-strip"></div>

    <h1 class="headline">
      <span class="light">Professional</span>
      <span class="light">Carpet</span>
      <span class="bold">Cleaning</span>
      <span class="bold">Services</span>
    </h1>

    <p class="intro">Our top-notch carpet cleaning services are here to bring life back to your floors, making them fresh, clean, and vibrant again.</p>

    <ul class="service-list">
      <li>Domestic Cleaning</li>
      <li>Office Cleaning</li>
      <li>End Of Tenancy Cleaning</li>
      <li>Regular Cleaning</li>
    </ul>

    <div class="call-rule"></div>
    <div class="call-label">GIVE US A CALL</div>

    <svg class="phone-bar" width="1120" height="120" viewBox="0 0 1120 120">
      <defs>
        <linearGradient id="phoneGrad" x1="0" x2="1" y1="0" y2="0">
          <stop offset="0" stop-color="#1a7bc0"/>
          <stop offset="1" stop-color="#0a3a80"/>
        </linearGradient>
      </defs>
      <rect width="1120" height="120" fill="#ffffff"/>
      <path d="M0 0 H730 Q705 0 690 35 L668 100 Q660 120 630 120 H0 Z" fill="url(#phoneGrad)"/>
    </svg>

    <svg class="phone-icon" width="34" height="22" viewBox="0 0 34 22" aria-hidden="true">
      <path d="M2 8 Q17 -2 32 8 L30 12 L24 10 L24 7 Q17 5 10 7 L10 10 L4 12 Z" fill="#fff"/>
      <path d="M8 12 H26 L30 21 H4 Z" fill="#fff"/>
      <circle cx="17" cy="16" r="3" fill="#1a7bc0"/>
    </svg>
    <div class="phone-number">555-319-4826</div>

    <svg class="gallery" width="1120" height="700" viewBox="0 0 1120 700">
      <defs>
        <linearGradient id="thumbWand" x1="0" y1="0" x2="0" y2="1">
          <stop offset="0" stop-color="#2a5fa8"/>
          <stop offset=".3" stop-color="#d9772e"/>
          <stop offset=".55" stop-color="#cfcac3"/>
          <stop offset="1" stop-color="#bdb7ae"/>
        </linearGradient>
        <linearGradient id="thumbCorridor" x1="0" y1="0" x2="0" y2="1">
          <stop offset="0" stop-color="#e8eaec"/>
          <stop offset=".4" stop-color="#c4c7ca"/>
          <stop offset=".6" stop-color="#85888b"/>
          <stop offset="1" stop-color="#6d7073"/>
        </linearGradient>
        <linearGradient id="thumbOffice" x1="0" y1="0" x2="0" y2="1">
          <stop offset="0" stop-color="#d6dbe0"/>
          <stop offset=".35" stop-color="#8f98a4"/>
          <stop offset=".55" stop-color="#4e5565"/>
          <stop offset="1" stop-color="#3e4452"/>
        </linearGradient>
        <linearGradient id="thumbTiles" x1="0" y1="0" x2="0" y2="1">
          <stop offset="0" stop-color="#eef2f6"/>
          <stop offset=".35" stop-color="#9fbde0"/>
          <stop offset=".6" stop-color="#3c79c2"/>
          <stop offset="1" stop-color="#5d8fc8"/>
        </linearGradient>
      </defs>
      <line x1="505" y1="601" x2="1110" y2="601" stroke="#1a7bc0" stroke-width="6"/>
      <g stroke="#1a7bc0" stroke-width="5">
        <circle cx="505" cy="601" r="68" fill="url(#thumbWand)" role="img" aria-label="Extraction wand cleaning a beige carpet"/>
        <circle cx="680" cy="601" r="68" fill="url(#thumbCorridor)" role="img" aria-label="Grey office corridor carpet"/>
        <circle cx="858" cy="601" r="68" fill="url(#thumbOffice)" role="img" aria-label="Empty open-plan office with dark carpet"/>
        <circle cx="1033" cy="601" r="68" fill="url(#thumbTiles)" role="img" aria-label="Blue and white checkered carpet tiles"/>
      </g>
    </svg>

    <div class="brand">
      <div class="brand-mark"></div>
      <div class="brand-divider"></div>
      <div class="brand-name">Loom Ranger<br>Property Services</div>
    </div>
  </div>
</body>
</html>
```